creative pack design with extended budget for Velmoraq coffee product

- we need a packing design for a new product of coffee for our company Tesmo Kirul located in Uganda.
- specialty Arabica coffee grown at slopes of Mountain Elgon with rich volcanic soils located in Eastern region of Uganda.
-  we have a logo already made and has registered in Uganda. our logo colors are mixture between a lot of brown color and yellow. vacuum  plastic bags.
- there is no restrictions towards your imagination .
-  all details available
- we will launch our product through phases ;
- phase 1 is  a ground coffee : ( Turkish coffee )  2 degrees of roasting which are ( medium dark , light ) of 250 grm
b) roasted beans: 2 degrees ( medium, dark) of 250 grm & 1000 grm
- we need also to highlight the eastern spirit of Turkish coffee
- we  need designs, the info and color only will be changed depending on previous classifications

Target Market(s)
Arab countries, Turkey , Uganda, Europe
Colors
Designer to choose colors to be used in the design.
Requirements
Nice to have
- about nature , Elgon mountain , farmers, freshness, distinctive product, soul of east such as decorated cup of Turkish coffee . these just an ideas but there is no restrictions on your imagination

```html
<!DOCTYPE html>
<html lang="en">
<head>
<meta charset="utf-8">
<title>Velmoraq Arabica – 250 g pack</title>
<link rel="stylesheet" href="https://fonts.googleapis.com/css2?family=Montserrat:wght@500;600;700&family=PT+Sans+Narrow:wght@400;700&family=Lilita+One&display=swap">
<style>
  :root {
    --gold: #b5995f;
    --gold-dark: #8a7142;
    --ink: #000000;
    --paper: #ffffff;
    --brown: #4a1f12;
    --frame: #c9b78f;
    --text-light: #ffffff;
  }
  * { box-sizing: border-box; margin: 0; padding: 0; }
  html, body { width: 1080px; height: 1200px; overflow: hidden; background: var(--paper); }
  .pack {
    position: relative; width: 1080px; height: 1200px;
    font-family: "Montserrat", sans-serif;
  }
  .pack__frame {
    position: absolute; left: 49px; top: 38px; width: 987px; height: 1128px;
    border: 1px solid var(--frame);
  }
  .panel { position: absolute; top: 38px; height: 1128px; text-align: center; }
  .panel--side { background: var(--ink); color: var(--text-light); }
  .panel--left { left: 49px; width: 268px; }
  .panel--front { left: 317px; width: 450px; background: var(--paper); }
  .panel--right { left: 767px; width: 269px; }
  .abs { position: absolute; left: 0; right: 0; }

  .brand-mark {
    display: flex; align-items: center; justify-content: center; gap: 8px;
    color: var(--gold); font-weight: 700; letter-spacing: 1px;
  }
  .brand-mark__dot { border-radius: 50%; background: var(--gold); flex: none; }
  .brand-mark--small { top: 196px; font-size: 19px; }
  .brand-mark--small .brand-mark__dot { width: 14px; height: 14px; }
  .brand-mark--large { top: 830px; font-size: 40px; color: var(--brown); }
  .brand-mark--large .brand-mark__dot { width: 30px; height: 30px; background: var(--brown); }

  .variety { top: 318px; font-size: 33px; font-weight: 600; color: var(--gold); letter-spacing: 1px; }
  .variety-sub { top: 360px; font-size: 15px; font-weight: 600; color: var(--gold-dark); }
  .origin-small { top: 386px; font-size: 15px; font-weight: 700; color: var(--gold); letter-spacing: .5px; }

  .copy { font-family: "PT Sans Narrow", sans-serif; font-size: 16px; line-height: 22.5px; padding: 0 24px; }
  .copy--bold { font-weight: 700; }
  .copy__title { font-family: "PT Sans Narrow", sans-serif; font-weight: 700; font-size: 21px; }
  .left-intro-title { top: 444px; }
  .left-intro { top: 470px; }
  .left-body { top: 694px; }
  .right-body { top: 444px; }
  .right-intro { top: 878px; }

  .weight { font-size: 34px; font-weight: 700; letter-spacing: 1px; }
  .weight small { font-size: 26px; }
  .panel--side .weight { top: 1064px; color: var(--gold); }
  .panel--front .weight { top: 1068px; color: var(--ink); }

  .caravan-art {
    position: absolute; left: 33px; top: 132px; width: 402px; height: 142px;
    background: linear-gradient(180deg, #fff 0%, #f3ead8 40%, #c7ac75 100%);
    border-bottom: 2px solid var(--ink);
  }
  .front-title {
    top: 278px; font-family: "Lilita One", sans-serif; font-size: 92px; line-height: 1;
    color: var(--gold); text-shadow: 5px 5px 0 var(--ink);
    -webkit-text-stroke: 3px var(--ink); letter-spacing: 1px;
  }
  .front-sub { top: 390px; font-size: 25px; font-weight: 600; color: var(--ink); letter-spacing: .5px; }
  .cup-art {
    position: absolute; left: 84px; top: 446px; width: 245px; height: 143px;
    border-radius: 40% 40% 45% 45%;
    background: radial-gradient(ellipse at 55% 40%, #d9c193 0%, #b5995f 60%, #fff 100%);
  }
  .origin-front { top: 972px; font-size: 31px; font-weight: 600; color: var(--gold); letter-spacing: 1px; }

  .roast {
    position: absolute; left: 30px; top: 1002px; display: flex; align-items: center; gap: 10px;
  }
  .roast__label { font-size: 15px; font-weight: 600; color: var(--gold); line-height: 18px; text-align: left; }
</style>
</head>
<body>
<main class="pack">
  <section class="panel panel--side panel--left">
    <div class="abs brand-mark brand-mark--small"><span class="brand-mark__dot"></span>VELMORAQ</div>
    <div class="abs variety">ARABICA</div>
    <div class="abs variety-sub">roasted coffee beans</div>
    <div class="abs origin-small">UGANDA</div>
    <div class="abs copy__title left-intro-title">Tesmo Kirul</div>
    <p class="abs copy copy--bold left-intro">Specialty Arabica coffee grown at slopes of Mountain Elgon with rich volcanic soils located in Eastern region of Uganda.</p>
    <p class="abs copy left-body">Specialty Arabica coffee grown at slopes of Mountain Elgon with rich volcanic soils located in Eastern region of Uganda. Specialty Arabica coffee grown slopes of Mountain Elgon with rich volcanic soils located in Eastern region specialty Arabica coffee grown at slopes of Mountain Elgon with rich volcanic soils located in Eastern region of Uganda.</p>
    <div class="abs weight">250 <small>g</small></div>
  </section>

  <section class="panel panel--front">
    <div class="caravan-art" role="img" aria-label="Silhouette of a camel caravan crossing in front of a golden setting sun"></div>
    <div class="abs front-title">arabica</div>
    <div class="abs front-sub">roasted coffee beans</div>
    <div class="cup-art" role="img" aria-label="Illustration of a cup of coffee with leaves and scattered coffee beans"></div>
    <div class="abs brand-mark brand-mark--large"><span class="brand-mark__dot"></span>VELMORAQ</div>
    <div class="abs origin-front">UGANDA</div>
    <div class="abs weight">250 <small>g</small></div>
  </section>

  <section class="panel panel--side panel--right">
    <div class="abs brand-mark brand-mark--small"><span class="brand-mark__dot"></span>VELMORAQ</div>
    <div class="abs variety">ARABICA</div>
    <div class="abs variety-sub">roasted coffee beans</div>
    <div class="abs origin-small">UGANDA</div>
    <p class="abs copy right-body">Specialty Arabica coffee grown at slopes of Mountain Elgon with rich volcanic soils located in Eastern region of Uganda. Specialty Arabica coffee grown slopes of Mountain Elgon with rich volcanic soils located in Eastern region specialty Arabica coffee grown at slopes of Mountain Elgon with rich volcanic soils located in Eastern region of Uganda.</p>
    <p class="abs copy copy--bold right-intro">Specialty Arabica coffee grown at slopes of Mountain Elgon with rich volcanic soils located in Eastern region of Uganda.</p>
    <div class="roast">
      <div class="roast__label">Roasting<br>degrees</div>
      <svg class="roast__scale" width="100" height="30" viewBox="0 0 100 30" aria-label="Roast level 3 of 5">
        <g stroke="#b5995f" stroke-width="1.6">
          <ellipse cx="10" cy="15" rx="8" ry="13" fill="#b5995f"/>
          <ellipse cx="30" cy="15" rx="8" ry="13" fill="#b5995f"/>
          <ellipse cx="50" cy="15" rx="8" ry="13" fill="#b5995f"/>
          <ellipse cx="70" cy="15" rx="8" ry="13" fill="none"/>
          <ellipse cx="90" cy="15" rx="8" ry="13" fill="none"/>
        </g>
        <g stroke="#000" stroke-width="1.4" fill="none">
          <path d="M10 3 Q7 15 10 27"/><path d="M30 3 Q27 15 30 27"/><path d="M50 3 Q47 15 50 27"/>
        </g>
        <g stroke="#b5995f" stroke-width="1.4" fill="none">
          <path d="M70 3 Q67 15 70 27"/><path d="M90 3 Q87 15 90 27"/>
        </g>
      </svg>
    </div>
    <div class="abs weight">250 <small>g</small></div>
  </section>

  <div class="pack__frame"></div>
</main>
</body>
</html>
```